Label design for our new range of organic honey.

We need a design for honey jars and tubs. The label needs to indicate we are located in the Western Australia. The design needs to be elegant, modern and attracting high end customers that focus on quality.

Need extra days to review

```html
<!DOCTYPE html>
<html lang="en">
<head>
<meta charset="utf-8">
<title>Organic Honey – Jar Label</title>
<link rel="stylesheet" href="https://fonts.googleapis.com/css2?family=Fraunces:ital,opsz,wght@0,9..144,400;0,9..144,500;1,9..144,400&display=swap">
<style>
  :root {
    --backdrop: #eaeaea;
    --label-light: #8a8b8d;
    --label-mid: #4a4a4b;
    --label-dark: #3a3a3a;
    --ink: #ffffff;
    --gold-dark: #8a6f32;
    --gold-mid: #c9a856;
    --gold-light: #f2e3a8;
  }
  * { box-sizing: border-box; margin: 0; padding: 0; }
  html, body {
    width: 1200px;
    height: 1200px;
    overflow: hidden;
    background: var(--backdrop);
  }
  .canvas {
    position: relative;
    width: 1200px;
    height: 1200px;
    background: var(--backdrop);
  }
  .label {
    position: absolute;
    left: 80px;
    top: 190px;
    width: 1040px;
    height: 820px;
    background: linear-gradient(90deg, var(--label-mid) 0%, var(--label-light) 14%, var(--label-mid) 40%, var(--label-dark) 70%, #5e5e5f 100%);
    color: var(--ink);
    font-family: "Fraunces", Georgia, serif;
  }
  .map-area {
    position: absolute;
    left: 155px;
    top: 52px;
    width: 800px;
    height: 700px;
    border-radius: 46% 40% 44% 48%;
    background: radial-gradient(ellipse at 50% 50%, rgba(255,255,255,0.08) 0%, rgba(255,255,255,0.03) 60%, rgba(255,255,255,0) 75%);
  }
  .brand {
    position: absolute;
    left: 178px;
    top: 362px;
    display: flex;
    align-items: center;
    gap: 12px;
  }
  .brand-dot {
    width: 22px;
    height: 22px;
    border-radius: 50%;
    border: 2px solid var(--ink);
    flex: none;
  }
  .brand-name {
    font-size: 19px;
    font-weight: 400;
    line-height: 1.25;
    letter-spacing: 0.06em;
    text-transform: uppercase;
    color: var(--ink);
  }
  .product {
    position: absolute;
    left: 440px;
    top: 258px;
    width: 460px;
    text-align: center;
  }
  .product-kind {
    font-size: 48px;
    font-weight: 500;
    line-height: 1;
  }
  .product-name {
    margin-top: 14px;
    font-size: 118px;
    font-weight: 500;
    line-height: 1;
    letter-spacing: 0.01em;
    background: linear-gradient(90deg, var(--gold-dark) 0%, var(--gold-light) 30%, var(--gold-mid) 55%, var(--gold-light) 80%, var(--gold-dark) 100%);
    -webkit-background-clip: text;
    background-clip: text;
    color: transparent;
  }
  .product-purity {
    margin-top: 12px;
    font-size: 36px;
    font-weight: 400;
    line-height: 1;
  }
  .origin {
    position: absolute;
    left: 340px;
    top: 570px;
    width: 310px;
    text-align: center;
    font-style: italic;
    font-size: 30px;
    line-height: 1.1;
  }
  .origin-rule {
    position: absolute;
    left: 348px;
    top: 658px;
    width: 290px;
    height: 12px;
    background: linear-gradient(90deg, var(--gold-dark) 0%, var(--gold-light) 45%, var(--gold-mid) 75%, var(--gold-dark) 100%);
  }
</style>
</head>
<body>
  <main class="canvas">
    <section class="label">
      <div class="map-area" role="img" aria-label="Outline map of Australia with Tasmania"></div>

      <div class="brand">
        <span class="brand-dot"></span>
        <span class="brand-name">Saltbush Grove<br>Honey</span>
      </div>

      <div class="product">
        <p class="product-kind">organic</p>
        <h1 class="product-name">HONEY</h1>
        <p class="product-purity">100% Pure</p>
      </div>

      <p class="origin">from<br>Western Australia</p>
      <div class="origin-rule"></div>
    </section>
  </main>
</body>
</html>
```